Regional and National Rugby Training and Player Development Company

We need a new responsive website design that is easy to navigate and encourages people to register for our programs.

Registration and payment could be written into the site but it can also be externally integrated as it is currently.

I want clean lines, bright images, and a webpage that is easy to update and manage. Currently using WordPress.
Updates

Keelstone Rugby runs four programs:  Youth Summer Rugby Camps, Winter Indoor Touch Rugby, Spring Training Camps, and the "Player Development Program" otherwise known as the Academy

Ultimately, Keelstone Rugby wants to attract the top players across the province of Ontario to join our corner-stone program, the Winter Academy.

We have had many players play at the provincial level and a select handful go on to represent Canada.  We aspire to set the standard for off-season junior rugby player development.

Reason: 1) Laptop crashed on Thurs. which meant I couldn't make a fair decision this weekend. 2). There are FIVE very good designs, each somewhat unique. I want to see what designers come up with when I outline what I like in each as a requirement of what has been provided. Thank you for your understanding and efforts in this regard. Sincerely, MB Sent from my iPad

Thank you for all your efforts and patience in this design campaign, I truly appreciate it.  Apologies for the lack of communication but as a full-time high school teacher, sometimes my "real job" gets put to the side.  

I have reduced over 30 designs to five... you are the five remaining I hope to take certain aspects of each that I like best and provide some feedback to you the designers, in order to make final adjustments before my final decision.

I hope you find this process agreeable and again, thank you for your patience and efforts in this campaign.  I think each of your designs look fantastic and are a drastic and valuable improvement of what I have been using up to this point.

Appreciatively,

MB

Voting poll results are in and there are three distinct leaders... going to focus on these three this week and come to a final decision before Friday.

Each designer will be contacted privately to provide some feedback and see what the best final product can look like.

Thank you for your patience and high-quality work!

MB

Reason: Just too much going on at the moment and trying to stay on top of this. Apologies to all. Just had the results of the voting poll come in and have reduced choices to two clear leaders with a third alternate. Going to provide feedback for all three today and hope to make final decision by Friday. Thank you for your efforts.

Target Market(s)

Junior rugby players (boys and girls) between the ages of 12 and 20... more importantly, their parents!

Industry/Entity Type

It Company

Requirements
Must have
• Must have high-resolution, clean lines, and encourage registration in programs. I would like it to be integrated with my YouTube page as well as other social media.

```html
<!DOCTYPE html>
<html lang="en">
<head>
<meta charset="utf-8">
<title>Keelstone Rugby Canada</title>
<link rel="stylesheet" href="https://fonts.googleapis.com/css2?family=Source+Sans+3:wght@400;600;700&family=Oswald:wght@500&display=swap">
<style>
  :root {
    --red: #c8202f;
    --bar: #5b5b5b;
    --ink: #3a3a3a;
    --body: #5e5e5e;
    --white: #ffffff;
    --line: #d9d9d9;
  }
  * { margin: 0; padding: 0; box-sizing: border-box; }
  html, body { width: 1094px; height: 1200px; overflow: hidden; background: var(--white); }
  body { position: relative; font-family: "Source Sans 3", Arial, sans-serif; color: var(--ink); }

  .topbar { position: absolute; left: 0; top: 0; width: 1094px; height: 50px; background: var(--bar); }
  .search { position: absolute; left: 632px; top: 9px; width: 207px; height: 31px; background: var(--white); border: 1px solid #cfcfcf; border-radius: 3px; font-size: 12px; font-style: italic; color: #9a9a9a; padding: 7px 10px; }
  .search svg { position: absolute; right: 9px; top: 8px; }
  .social-top { position: absolute; left: 895px; top: 12px; display: flex; gap: 7px; }
  .social-top span { width: 26px; height: 26px; border-radius: 50%; background: #8e8e8e; display: block; }

  .header { position: absolute; left: 0; top: 50px; width: 1094px; height: 132px; }
  .brand { position: absolute; left: 80px; top: 40px; display: flex; align-items: center; gap: 12px; }
  .brand-mark { width: 40px; height: 40px; background: var(--red); display: block; }
  .brand-name { font-size: 24px; font-weight: 700; color: var(--red); text-transform: uppercase; line-height: 1; letter-spacing: .5px; }
  .nav { position: absolute; right: 70px; top: 61px; display: flex; font-size: 16px; text-transform: uppercase; color: var(--ink); }
  .nav a { color: inherit; text-decoration: none; padding: 0 17px; border-left: 1px dotted #bdbdbd; line-height: 18px; }
  .nav a:first-child { border-left: 0; }
  .nav a:last-child { padding-right: 0; }
  .nav a.is-current { color: var(--red); }

  .hero { position: absolute; left: 0; top: 182px; width: 1094px; height: 438px; background: radial-gradient(ellipse at 28% 45%, #d9d4ce 0%, #a39a8e 22%, #4e5a4e 55%, #2f3a33 100%); }
  .hero-caption { position: absolute; left: 79px; top: 256px; width: 449px; height: 131px; background: rgba(40,40,40,.78); padding: 20px 22px; color: var(--white); }
  .hero-caption h1 { font-family: "Oswald", "Arial Narrow", sans-serif; font-weight: 500; font-size: 28px; line-height: 1.1; text-transform: uppercase; letter-spacing: .2px; }
  .hero-caption p { font-size: 15px; line-height: 1.55; margin-top: 10px; }
  .hero-dots { position: absolute; left: 977px; top: 416px; display: flex; gap: 2px; }
  .hero-dots span { width: 11px; height: 11px; border-radius: 50%; border: 1px solid #cfcfcf; background: #777; }
  .hero-dots span:first-child { background: #ececec; }

  .feature { position: absolute; top: 651px; width: 300px; }
  .feature-icon { position: absolute; left: 0; top: 3px; }
  .feature h2 { margin-left: 78px; font-size: 23px; font-weight: 400; color: var(--red); line-height: 1.1; }
  .feature h3 { margin-left: 78px; font-size: 15px; font-weight: 600; color: #333; margin-top: 4px; }
  .feature p { font-size: 12.5px; line-height: 19.7px; color: #4b4b4b; margin-top: 18px; padding-left: 6px; }

  .section-title { position: absolute; font-size: 19px; font-weight: 400; color: var(--red); }
  .welcome-photo { position: absolute; left: 80px; top: 857px; width: 200px; height: 193px; border-radius: 4px; background: linear-gradient(160deg, #3c3a36 0%, #1d1d1d 55%, #2b2b2b 100%); }
  .welcome-text { position: absolute; left: 300px; top: 848px; width: 392px; }
  .welcome-text .lead { font-size: 15.3px; line-height: 23px; color: #5a5a5a; }
  .welcome-text p { font-size: 12.6px; line-height: 21.9px; color: var(--body); margin-top: 8px; }

  .news-item { position: absolute; left: 753px; width: 290px; display: flex; gap: 14px; }
  .news-thumb { width: 63px; height: 55px; border: 1px solid var(--line); padding: 2px; flex: none; }
  .news-thumb span { display: block; width: 100%; height: 100%; }
  .news-body { font-size: 12.5px; line-height: 19.7px; color: #4b4b4b; margin-top: -3px; }
  .news-body strong { color: #333; font-weight: 700; display: block; }

  .footer { position: absolute; left: 0; top: 1105px; width: 1094px; height: 95px; background: var(--bar); color: var(--white); font-size: 12.5px; }
  .footer-links { position: absolute; left: 79px; top: 26px; }
  .footer-copy { position: absolute; left: 80px; top: 60px; }
  .social-foot { position: absolute; left: 799px; top: 35px; display: flex; gap: 16px; }
  .social-foot span { width: 28px; height: 28px; background: var(--white); border-radius: 3px; display: block; box-shadow: 0 1px 2px rgba(0,0,0,.4); }
</style>
</head>
<body>

<div class="topbar">
  <div class="search">Search..
    <svg width="13" height="13" viewBox="0 0 13 13"><circle cx="5.5" cy="5.5" r="4" fill="none" stroke="#9a9a9a" stroke-width="1.8"/><line x1="8.5" y1="8.5" x2="12" y2="12" stroke="#9a9a9a" stroke-width="2"/></svg>
  </div>
  <div class="social-top"><span></span><span></span><span></span><span></span></div>
</div>

<header class="header">
  <div class="brand"><span class="brand-mark"></span><span class="brand-name">Keelstone Rugby Canada</span></div>
  <nav class="nav">
    <a class="is-current" href="#">Home</a>
    <a href="#">Player Development</a>
    <a href="#">Community</a>
    <a href="#">News</a>
    <a href="#">Contact</a>
  </nav>
</header>

<section class="hero" role="img" aria-label="Photo of a rugby player in a scrum cap running with the ball past a tackler, crowd blurred behind">
  <div class="hero-caption">
    <h1>Bring Your Home Movies To Life</h1>
    <p>Jerta baditaut onsequser untur magni dolores eoquie volup tate msequi nesciunt. Voluptatem accusantium dolorem.</p>
  </div>
  <div class="hero-dots"><span></span><span></span><span></span><span></span></div>
</section>

<div class="feature" style="left:79px">
  <svg class="feature-icon" width="50" height="46" viewBox="0 0 50 46" fill="#c8202f">
    <rect x="18" y="2" width="30" height="9"/><rect x="26" y="18" width="22" height="9"/><rect x="18" y="34" width="30" height="9"/>
    <rect x="0" y="21" width="12" height="3"/><polygon points="10,16 19,22.5 10,29"/>
  </svg>
  <h2>Mission</h2><h3>Lorem Ipsum dolore</h3>
  <p>Scing elit vivamus faucibus, mi quis convallisto te mpus, magna elit tincidunt arcu, ac rutrumop tell us nisl sed nisi. Morbi tempor quam vel massa.</p>
</div>

<div class="feature" style="left:416px">
  <svg class="feature-icon" width="50" height="48" viewBox="0 0 50 48" fill="#c8202f">
    <polygon points="25,0 48,13 25,26 2,13"/>
    <polygon points="2,21 25,34 48,21 48,27 25,40 2,27"/>
    <polygon points="2,31 25,44 48,31 48,35 25,48 2,35"/>
  </svg>
  <h2>Vision</h2><h3>Lorem Ipsum dolore</h3>
  <p>Scing elit vivamus faucibus, mi quis convallisto te mpus, magna elit tincidunt arcu, ac rutrumop tell us nisl sed nisi. Morbi tempor quam vel massa.</p>
</div>

<div class="feature" style="left:753px">
  <svg class="feature-icon" width="50" height="36" viewBox="0 0 50 36" fill="#c8202f" style="top:8px">
    <polygon points="0,18 16,2 16,11 34,11 34,2 50,18 34,34 34,25 16,25 16,34"/>
  </svg>
  <h2>Learning Continuum</h2><h3>Lorem Ipsum dolore</h3>
  <p>Scing elit vivamus faucibus, mi quis convallisto te mpus, magna elit tincidunt arcu, ac rutrumop tell us nisl sed nisi. Morbi tempor quam vel massa.</p>
</div>

<h2 class="section-title" style="left:79px;top:810px">Welcome To Our Website</h2>
<div class="welcome-photo" role="img" aria-label="Team photo of junior players in black kit with their coach"></div>
<div class="welcome-text">
  <div class="lead">Ut wisi enim ad minim veniam, quis nostrud exerci tation ulli amcorper suscipit lobortis nisl ut aliquip exea.</div>
  <p>Incididunt ut labore et dolore magna aliqua. Ut enim ad minim veniam, quis nostrud exercitation ullamcolaboris nisi ut aliquip ex ea commodo consequat. Duis tefd aute iruredolor inreprehenderit in voluptate velit esse cillum.Dolore magna aliqua. Ut enim ad minim veniam, Quisnostru dexercitation ullamco laboris nisi ut aliquip. Ut enim ad minim veniam, quis nostrud exercitation ullamco laboris. Claritas est etiam processus dynamicus, qui sequitur mutationem.</p>
</div>

<h2 class="section-title" style="left:753px;top:810px">Latest News</h2>
<div class="news-item" style="top:851px">
  <div class="news-thumb"><span role="img" aria-label="Portrait photo of a young girl" style="background:linear-gradient(135deg,#8aa35c,#d8b98c)"></span></div>
  <div class="news-body"><strong>During November 2013</strong>our Principal Petrophysicist, quisstr xercitation ullamco labors.</div>
</div>
<div class="news-item" style="top:923px">
  <div class="news-thumb"><span role="img" aria-label="Portrait photo of a young boy" style="background:linear-gradient(135deg,#4f8a5a,#c9a48a)"></span></div>
  <div class="news-body"><strong>During November 2013</strong>At vero eois et accusamus et iustoid gnissimos ducimus qui.</div>
</div>
<div class="news-item" style="top:996px">
  <div class="news-thumb"><span role="img" aria-label="Portrait photo of a woman" style="background:linear-gradient(135deg,#e8e8e8,#b8a89a)"></span></div>
  <div class="news-body"><strong>During November 2013</strong>Deleniti atque corrupti quos doeset s molestias excepturi sint.</div>
</div>

<footer class="footer">
  <div class="footer-links">Home | Player Development | Community | KRC News | Conatct us</div>
  <div class="footer-copy">Copyrights 2013. All Rights Reserved.</div>
  <div class="social-foot"><span></span><span></span><span></span><span></span></div>
</footer>

</body>
</html>
```